The Willow Compass

Look for someone who can add some splash and make this powerpoint presentation more dynamic. Feel free to use color, animations etc to provide some punch.

```html
<!DOCTYPE html>
<html lang="en">
<head>
<meta charset="utf-8">
<title>The Willow Compass – Deck Overview</title>
<link href="https://fonts.googleapis.com/css2?family=Poppins:wght@400;500;600;700&display=swap" rel="stylesheet">
<style>
  :root{
    --page:#ffffff;
    --slide:#f2f1ec;
    --ink:#1d1d1b;
    --ink-soft:#3a3a38;
    --muted:#6b6a66;
    --black:#0d0d0d;
    --accent:#1fb89a;
    --cover-dark:#1a1816;
    --cover-warm:#5a3d2a;
  }
  *{box-sizing:border-box;margin:0;padding:0}
  html,body{width:1200px;height:1101px;overflow:hidden;background:var(--page)}
  body{position:relative;font-family:"Poppins",sans-serif;color:var(--ink)}
  .slide{position:absolute;width:513px;height:289px;background:var(--slide);overflow:hidden;box-shadow:0 4px 14px rgba(0,0,0,.12)}
  .s1{left:71px;top:64px}
  .s2{left:623px;top:64px}
  .s3{left:71px;top:397px}
  .s4{left:623px;top:397px}
  .s5{left:71px;top:733px}
  .s6{left:623px;top:733px}

  .brand{position:absolute;top:18px;right:8px;display:flex;align-items:center;gap:4px;font-size:5.5px;letter-spacing:1.6px;font-weight:500;color:var(--ink)}
  .brand-dot{width:6px;height:6px;border-radius:50%;background:var(--ink)}
  .brand.left{left:11px;right:auto}
  .edge{position:absolute;right:0;top:0;width:1.5px;height:22px;background:var(--accent)}

  .title{position:absolute;font-weight:600;font-size:15.5px;color:var(--ink);padding-left:10px;line-height:1.2}
  .title::before{content:"";position:absolute;left:0;top:1px;bottom:1px;width:1.5px;background:var(--ink)}

  .bullets{position:absolute;list-style:none;font-size:8.4px;line-height:1.28;color:var(--ink-soft)}
  .bullets li{position:relative;padding-left:9px}
  .bullets li::before{content:"";position:absolute;left:0;top:4px;width:3px;height:3px;border-radius:50%;background:var(--ink)}
  .bullets .sub{padding-left:17px}
  .bullets .sub::before{left:8px;background:none;border:.7px solid var(--ink);width:3.4px;height:3.4px}

  .footer{position:absolute;left:0;right:0;bottom:0;height:30px;font-size:6.2px;color:var(--ink)}
  .footer .globe{position:absolute;left:7px;top:6px;width:16px;height:16px}
  .footer .url{position:absolute;left:28px;top:11px}
  .footer .rights{position:absolute;left:215px;top:10px;color:var(--muted);font-size:5.8px}
  .footer .page-no{position:absolute;right:0;bottom:0;width:36px;height:22px;background:var(--black);color:#fff;font-size:5.5px;display:flex;align-items:center;justify-content:center}

  .photo{position:absolute}
  /* cover */
  .cover-bg{position:absolute;inset:0;background:linear-gradient(180deg,#2b2a2a 0%,#3c2c22 45%,var(--cover-warm) 65%,var(--cover-dark) 100%)}
  .cover-brand{position:absolute;left:0;right:0;top:118px;text-align:center;color:#e9e6e0;font-size:17px;letter-spacing:5px;font-weight:400}
  .cover-title{position:absolute;left:73px;top:196px;color:#fff;font-size:26px;font-weight:700;letter-spacing:.3px}
  .cover-sub{position:absolute;left:75px;top:233px;color:#fff;font-size:15px;font-weight:600}

  .portrait{background:radial-gradient(ellipse at 55% 45%,#c99c86 0%,#8d6a5a 30%,#2b2522 65%,#141211 100%)}
  .city{background:linear-gradient(180deg,#6d86a8 0%,#a0603a 60%,#3a4658 100%)}
  .chart-img{background:linear-gradient(135deg,#1a2a55 0%,#0f3a5a 45%,#2a8fb0 70%,#6a2a4a 100%)}
  .sky-img{background:linear-gradient(180deg,#5f9bd6 0%,#cfe2f2 55%,#a9b4bc 80%,#e0c9a8 100%)}
  .market-img{background:linear-gradient(135deg,#0d1b1a 0%,#17302c 50%,#2b5a44 80%,#d08a3a 100%)}
</style>
</head>
<body>

<!-- Cover -->
<section class="slide s1">
  <div class="cover-bg" role="img" aria-label="Dusk city skyline seen from an office window with stock chart lines overlaid"></div>
  <div class="cover-brand">BRIGHT HARBOR</div>
  <h1 class="cover-title">THE WILLOW COMPASS</h1>
  <p class="cover-sub">How to raise faster, get back to building and grow</p>
</section>

<!-- About -->
<section class="slide s2">
  <div class="photo portrait" style="left:0;top:0;width:214px;height:258px" role="img" aria-label="Portrait of the course host with a torn paper edge"></div>
  <div class="brand"><span class="brand-dot"></span>BRIGHT HARBOR</div>
  <h2 class="title" style="left:235px;top:44px">About Me &amp; My Background</h2>
  <ul class="bullets" style="left:235px;top:80px;width:215px;font-size:8.6px;line-height:1.8">
    <li>Over the last 25yrs, I helped two companies build business units to revenues over $1B annually.</li>
    <li style="margin-top:7px">Then, in 2018, I burned out.</li>
    <li style="margin-top:7px">So, I decided to leave the corporate executive grind to help early-stage founders.</li>
    <li style="margin-top:7px">Since that day, I've spent my time finding ways to help early-stage Founders win!</li>
  </ul>
  <footer class="footer">
    <svg class="globe" viewBox="0 0 16 16"><circle cx="8" cy="8" r="8" fill="#0d0d0d"/><g fill="none" stroke="#fff" stroke-width=".7"><circle cx="8" cy="8" r="4.5"/><ellipse cx="8" cy="8" rx="2" ry="4.5"/><path d="M3.5 8h9M4.2 5.7h7.6M4.2 10.3h7.6"/></g></svg>
    <span class="url">www.brightharbor.com</span>
    <span class="rights">© 2024. ALL Rights Reserved.</span>
    <span class="page-no">Page 02</span>
  </footer>
</section>

<!-- Results -->
<section class="slide s3">
  <div class="photo portrait" style="left:290px;top:0;width:223px;height:258px" role="img" aria-label="Portrait of the course host with a torn paper edge"></div>
  <div class="brand left"><span class="brand-dot"></span>BRIGHT HARBOR</div>
  <h2 class="title" style="left:59px;top:57px">My Results</h2>
  <ul class="bullets" style="left:59px;top:90px;width:215px;font-size:8.8px;line-height:1.7">
    <li>64 companies invested in</li>
    <li style="margin-top:7px">35 companies have gotten to Series A</li>
    <li style="margin-top:7px">$1.08B+ capital raised by my portfolio companies</li>
    <li style="margin-top:7px">8 exits to date</li>
    <li style="margin-top:7px">Consulting business working with early-stage founders across 5 continents</li>
    <li style="margin-top:7px">8 exits to date</li>
  </ul>
  <footer class="footer">
    <svg class="globe" viewBox="0 0 16 16"><circle cx="8" cy="8" r="8" fill="#0d0d0d"/><g fill="none" stroke="#fff" stroke-width=".7"><circle cx="8" cy="8" r="4.5"/><ellipse cx="8" cy="8" rx="2" ry="4.5"/><path d="M3.5 8h9M4.2 5.7h7.6M4.2 10.3h7.6"/></g></svg>
    <span class="url">www.brightharbor.com</span>
    <span class="rights">© 2024. ALL Rights Reserved.</span>
    <span class="page-no">Page 03</span>
  </footer>
</section>

<!-- Why -->
<section class="slide s4">
  <div class="edge"></div>
  <div class="brand"><span class="brand-dot"></span>BRIGHT HARBOR</div>
  <h2 class="title" style="left:157px;top:10px">Why I Created This Course</h2>
  <p style="position:absolute;left:0;width:513px;text-align:center;top:32px;font-size:11.2px;font-weight:500">Spent 6 years chatting with over 3,000 founders and learned:</p>
  <ul class="bullets" style="left:40px;top:62px;width:225px;font-size:7.9px;line-height:1.3">
    <li>The fundraising process is NOT transparent</li>
    <li style="margin-top:8px">Founders don't know where to begin, who to talk to or where to start</li>
    <li style="margin-top:8px">Founders don't get the candid feedback they need</li>
    <li style="margin-top:8px">There is not easy way to find the right type of investors</li>
    <li style="margin-top:8px">Founders don't always know what investors want, how to present it and the what the necessary KPI's for success are</li>
    <li style="margin-top:8px">Founders underestimate how hard, long and tedious this process is start to finish</li>
    <li style="margin-top:8px">The result is a fragmented, slow and challenging journey that leaves founders feeling empty and ultimately unfunded.</li>
  </ul>
  <svg style="position:absolute;left:282px;top:62px" width="194" height="194" viewBox="0 0 194 194" aria-hidden="true"><circle cx="97" cy="97" r="95.5" fill="none" stroke="#0d0d0d" stroke-width="2"/></svg>
  <div class="photo city" style="left:292px;top:72px;width:174px;height:174px;border-radius:50%" role="img" aria-label="Glass skyscrapers reflecting a golden sunset over a plaza"></div>
  <footer class="footer">
    <svg class="globe" viewBox="0 0 16 16"><circle cx="8" cy="8" r="8" fill="#0d0d0d"/><g fill="none" stroke="#fff" stroke-width=".7"><circle cx="8" cy="8" r="4.5"/><ellipse cx="8" cy="8" rx="2" ry="4.5"/><path d="M3.5 8h9M4.2 5.7h7.6M4.2 10.3h7.6"/></g></svg>
    <span class="url">www.brightharbor.com</span>
    <span class="rights">© 2024. ALL Rights Reserved.</span>
    <span class="page-no">Page 04</span>
  </footer>
</section>

<!-- Expected results -->
<section class="slide s5">
  <div class="brand"><span class="brand-dot"></span>BRIGHT HARBOR</div>
  <h2 class="title" style="left:157px;top:18px">Expected Results For Founders</h2>
  <div style="position:absolute;left:45px;top:161px;width:88px;height:76px;background:var(--black);border-radius:2px"></div>
  <div class="photo chart-img" style="left:56px;top:59px;width:185px;height:167px;border-radius:2px" role="img" aria-label="Glowing blue and red financial data chart"></div>
  <ul class="bullets" style="left:269px;top:59px;width:210px;font-size:8.2px;line-height:1.28">
    <li>Founders now have a firm understanding of the fundraising process end-to-end</li>
    <li style="margin-top:11px">Founder have resources to help them find the right investors at the right time</li>
    <li style="margin-top:11px">Founders understand the different types of investors, motivation and stages</li>
    <li style="margin-top:11px">Founders understand how to tell their story more effectively</li>
    <li style="margin-top:11px">Founders feel equipped to successfully raise capital from the right type of investors</li>
    <li style="margin-top:11px">Founders reduce to fundraise from 6-8 months to 3-6 mths</li>
  </ul>
  <footer class="footer">
    <svg class="globe" viewBox="0 0 16 16"><circle cx="8" cy="8" r="8" fill="#0d0d0d"/><g fill="none" stroke="#fff" stroke-width=".7"><circle cx="8" cy="8" r="4.5"/><ellipse cx="8" cy="8" rx="2" ry="4.5"/><path d="M3.5 8h9M4.2 5.7h7.6M4.2 10.3h7.6"/></g></svg>
    <span class="url">www.brightharbor.com</span>
    <span class="rights">© 2024. ALL Rights Reserved.</span>
    <span class="page-no">Page 05</span>
  </footer>
</section>

<!-- Story -->
<section class="slide s6">
  <div class="edge"></div>
  <div class="brand"><span class="brand-dot"></span>BRIGHT HARBOR</div>
  <h2 class="title" style="left:157px;top:18px">It's All About The Story</h2>
  <ul class="bullets" style="left:23px;top:62px;width:200px;font-size:8px;line-height:1.28">
    <li>This is your chance to share your vision</li>
    <li style="margin-top:7px">Can you tell your story from the customers perspective</li>
    <li style="margin-top:7px">Use simple words, not jargon</li>
    <li style="margin-top:7px">Explain what you do so your "nana" could understand it</li>
    <li style="margin-top:7px">Revenue solves everything</li>
    <li style="margin-top:7px">Storytelling is a "full body" experience - Stand up, move around and point to screen</li>
    <li style="margin-top:7px">Speak in numbers – Founders who build big companies are data driven</li>
    <li class="sub">Example: We grew 40% per month for the last 6 months and are now at $100K MRR.</li>
  </ul>
  <div class="photo sky-img" style="left:230px;top:82px;width:131px;height:139px;border-radius:2px" role="img" aria-label="Man standing in a paper boat made of a banknote under a bright sky"></div>
  <div class="photo market-img" style="left:376px;top:82px;width:131px;height:139px;border-radius:2px" role="img" aria-label="Businessman in front of a glowing rising market chart"></div>
  <footer class="footer">
    <svg class="globe" viewBox="0 0 16 16"><circle cx="8" cy="8" r="8" fill="#0d0d0d"/><g fill="none" stroke="#fff" stroke-width=".7"><circle cx="8" cy="8" r="4.5"/><ellipse cx="8" cy="8" rx="2" ry="4.5"/><path d="M3.5 8h9M4.2 5.7h7.6M4.2 10.3h7.6"/></g></svg>
    <span class="url">www.brightharbor.com</span>
    <span class="rights">© 2024. ALL Rights Reserved.</span>
    <span class="page-no">Page 06</span>
  </footer>
</section>

</body>
</html>
```